Bluestone Advisory & Mgmt - Professional Business Cards

Hi!

I am a Real Estate Developer and Construction Consultant.

I have a lot of inspiration from previous designs and would be open to using the attached Designs as a starting point. I would like to see these styles incorporated into your designs.

I really need professional business card to go with it that includes my important info.

Look forward to seeing your designs!.

Target Market(s)

My Target market are building owners, lawyers, consultants.

Industry/Entity Type

Real Estate Development

Contact Information for Business Card

My Name: Dorian Pelkey
My Title: Principle
Company Name: Bluestone Advisory & Mgmt, LLC
Address: 348 West 71st Street, 9th FL New York, NY 10023
Mobile: 646.806.3971
Website: bam-hvx.example

Font styles to use
Serif
Sans Serif

Colors

Designer to choose colors to be used in the design.

Requirements
Must have
• Must incorporate the logo attached or have new that looks similar.
• Must use professional font that will be seen and judged by wealthy land owners and developers.
• Must incorporate some of the color green.
Should not have
• Photo's or pictures of people or buildings of any kind.

```html
<!DOCTYPE html>
<html lang="en">
<head>
<meta charset="utf-8">
<title>Bluestone Advisory &amp; Mgmt - Business Cards</title>
<link href="https://fonts.googleapis.com/css2?family=Lato:wght@400;700&display=swap" rel="stylesheet">
<style>
  :root {
    --green: #4fb677;
    --grey: #968c8b;
    --text-grey: #8a8382;
    --card: #ffffff;
    --backdrop: #ecebea;
  }
  * { margin: 0; padding: 0; box-sizing: border-box; }
  html, body { width: 1000px; height: 1200px; overflow: hidden; }
  body {
    position: relative;
    background: var(--backdrop);
    font-family: "Lato", Arial, sans-serif;
  }
  .card {
    position: absolute;
    background: var(--card);
    box-shadow: 0 6px 18px rgba(0,0,0,0.18);
    overflow: hidden;
  }
  .card--front { left: 111px; top: 120px; width: 777px; height: 446px; }
  .card--back  { left: 109px; top: 633px; width: 782px; height: 447px; }
  .card__bands { position: absolute; left: 0; width: 100%; }
  .card__bands--bottom { bottom: 0; height: 40px; }
  .card__bands--top { top: 0; height: 40px; }

  .brand {
    position: absolute;
    color: var(--green);
    font-weight: 400;
    line-height: 1.05;
  }
  .card--front .brand { left: 74px; top: 148px; width: 280px; }
  .card--back .brand { left: 0; right: 0; top: 128px; text-align: center; }
  .brand__name { display: block; font-size: 58px; letter-spacing: -0.5px; }
  .card--back .brand__name { font-size: 76px; }
  .brand__tagline { display: block; font-size: 22px; margin-top: 8px; }
  .card--back .brand__tagline { font-size: 27px; }

  .divider {
    position: absolute;
    left: 363px; top: 112px;
    width: 2px; height: 221px;
    background: var(--green);
  }
  .details { position: absolute; left: 404px; top: 106px; }
  .details__name { color: var(--green); font-weight: 700; font-size: 25px; }
  .details__title { color: var(--text-grey); font-size: 18px; margin-top: 6px; }
  .details__company { color: var(--green); font-weight: 700; font-size: 18px; margin-top: 16px; }
  .contact { list-style: none; margin-top: 14px; color: var(--text-grey); font-size: 18px; }
  .contact__item { display: flex; align-items: flex-start; line-height: 31px; }
  .contact__icon { width: 18px; height: 18px; margin: 6px 9px 0 0; flex: none; }
</style>
</head>
<body>

<section class="card card--front" aria-label="Business card front">
  <div class="brand">
    <span class="brand__name">Bluestone</span>
    <span class="brand__tagline">Advisory &amp; Management</span>
  </div>

  <div class="divider"></div>

  <div class="details">
    <p class="details__name">Dorian Pelkey</p>
    <p class="details__title">Principle</p>
    <p class="details__company">Bluestone Advisory &amp; Mgmt, LLC</p>
    <ul class="contact">
      <li class="contact__item">
        <svg class="contact__icon" viewBox="0 0 24 24" fill="none" stroke="#4fb677" stroke-width="2.2"><path d="M12 22s-7-7.2-7-12.5a7 7 0 0 1 14 0C19 14.8 12 22 12 22z"/><circle cx="12" cy="9.5" r="2.6"/></svg>
        <span>348 West 71st Street<br>9th FL New York, NY 10023</span>
      </li>
      <li class="contact__item">
        <svg class="contact__icon" viewBox="0 0 24 24" fill="#4fb677"><path d="M6.6 10.8a15.2 15.2 0 0 0 6.6 6.6l2.2-2.2c.3-.3.7-.4 1-.2 1.1.4 2.3.6 3.6.6.6 0 1 .4 1 1V20c0 .6-.4 1-1 1A17 17 0 0 1 3 4c0-.6.4-1 1-1h3.5c.6 0 1 .4 1 1 0 1.3.2 2.5.6 3.6.1.3 0 .7-.2 1z"/></svg>
        <span>646.806.3971</span>
      </li>
      <li class="contact__item">
        <svg class="contact__icon" viewBox="0 0 24 24" fill="none" stroke="#4fb677" stroke-width="2"><circle cx="12" cy="12" r="9"/><path d="M3 12h18M12 3c2.6 2.7 2.6 15.3 0 18M12 3c-2.6 2.7-2.6 15.3 0 18"/></svg>
        <span>bam-hvx.example</span>
      </li>
    </ul>
  </div>

  <svg class="card__bands card__bands--bottom" viewBox="0 0 777 40" preserveAspectRatio="none" aria-hidden="true">
    <polygon points="0,22 374,22 356,40 0,40" fill="#968c8b"/>
    <polygon points="407,0 777,0 777,40 368,40" fill="#4fb677"/>
  </svg>
</section>

<section class="card card--back" aria-label="Business card back">
  <svg class="card__bands card__bands--top" viewBox="0 0 782 40" preserveAspectRatio="none" aria-hidden="true">
    <polygon points="0,0 390,0 350,40 0,40" fill="#4fb677"/>
    <polygon points="392,0 782,0 782,19 373,19" fill="#968c8b"/>
  </svg>

  <div class="brand">
    <span class="brand__name">Bluestone</span>
    <span class="brand__tagline">Advisory &amp; Management</span>
  </div>

  <svg class="card__bands card__bands--bottom" viewBox="0 0 782 40" preserveAspectRatio="none" aria-hidden="true">
    <polygon points="0,22 378,22 360,40 0,40" fill="#968c8b"/>
    <polygon points="410,0 782,0 782,40 371,40" fill="#4fb677"/>
  </svg>
</section>

</body>
</html>
```